Artist needs a Wordpress Website design to market my original paintings

Mira Castellan Gallery.com
Artist - Original Abstract Paintings

Artist needs classy and elegant WORDPRESS website to market my Original Paintings.
What sets these paintings apart?
Each one was inspired by the inner connection between the artist and the individual destined to receive the painting. Paintings are priced high end and require a website to reflect their high quality.
Website must be responsive on all devices. eg. mobile, laptop and desktop. It must have a shopping cart in order to complete sales.
The domain name miracastellangallery.com has already been purchased and is hosted on Corvanet.
I want it to be very easy to navigate and also easy for me to add and edit more images and content.
I have no official logo but you can insert the title,
Mira Castellan
Collection
Original Fluid Art Paintings
in whatever design/font format you feel attractive, I leave that to the designer. I want it to be simple and include a lot of negative space to avoid a cluttered look. The paintings are colorful on their own and prefer not to detract from them as a focal point. I leave the color theme to the designer. Perhaps you may like to extract a color theme from one of the paintings.
Requirements:
5 pages: HOME, ABOUT, SHOP, CART, CONTACT
Home page:
-Menu across the top
-1 large painting (prefer the purple and green painting)
-3 smaller images below the large one
Unless you come up with a more professional format.
ABOUT:
(You can include my uploaded photo for now on the ABOUT page. I will replace it when I get a professional photo.)
I learned I am never too old to re-invent my life. Lesson learned. At the age of 78 and after the ending of my 30 years of marriage I was faced with an unexpected change in my life circumstances. I made the decision to re-invent my life.
Art, in varying media has always been a part of my experience as a hobby. When I was presented with fluid art, my life as I had known it turned to excitement, and discovery, carving a promising vision of my future.
My spiritual training has taught me how to recognize my connection with people inwardly. With this awareness it became clear to me while painting that I was creating a work of art for a specific individual. I allow creative expression to flow through me that is destined for you. I do not know who you are, but if you recognize the painting that inspires you, I have succeeded with our connection.
I live in Washington State, USA
I am looking forward to meeting you.
Mira Castellan
SHOP:
This should be the gallery from which one can shop. The images will be more like a thumbprint but large enough to see well, perhaps 3 across the page. As one hovers over, or clicks on one, it will link to a page with a larger view that has:
-Description
-Price and a CHOICE to click on
-Add to Cart Button OR
-Continue shopping (so they don't have to go back to homepage)
This page should be a scrolling one so eventually all of my paintings will be added to this page and easy for someone to shop instead of going back and forth between pages.
Please set this up (making it a link to larger image, etc) and include one or all of the images I upload here. I will add the rest.

CART:
-Add a shopping cart

CONTACT:
-email: castellangallery@mailvessel.net
All pages should have a link back to the homepage.
SOCIAL MEDIA LINKS:
-Pictaro:
http://pictaro.example/miracastellangallery
-Socialroom
https://www.socialroom.example/theuniquecanvas/?
view_public_for=384751029366217

http://ellisbrookstudio.net
eg of a website that I like the navigation. I like the simplicity of the Home Page but the photo is too large. A smaller main photo and 3 smaller ones beneath it would have looked nicer to me.

```html
<!DOCTYPE html>
<html lang="en">
<head>
<meta charset="utf-8">
<title>Mira Castellan Collection – Home</title>
<link rel="stylesheet" href="https://fonts.googleapis.com/css2?family=Playfair+Display:wght@400&family=Poppins:wght@400&family=Quicksand:wght@500&display=swap">
<style>
  :root {
    --ink: #111111;
    --text: #1e1e1e;
    --muted: #7a7a7a;
    --accent: #a48b4c;
    --band: #f8f4f1;
    --card: #f8f4f1;
    --rule: #b9b9b9;
    --page: #ffffff;
  }
  * { margin: 0; padding: 0; box-sizing: border-box; }
  html, body { width: 1050px; height: 1200px; overflow: hidden; background: var(--page); }
  body { position: relative; font-family: "Poppins", sans-serif; color: var(--text); }

  .brand { position: absolute; top: 22px; left: 0; width: 1050px; text-align: center; }
  .brand-name { font-family: "Playfair Display", serif; font-size: 38px; font-weight: 400; color: var(--ink); line-height: 1.2; }
  .brand-tagline { font-family: "Quicksand", sans-serif; font-size: 15px; letter-spacing: 2.6px; color: var(--ink); margin-top: 14px; }

  .main-nav { position: absolute; top: 154px; left: 0; width: 1050px; display: flex; justify-content: center; gap: 26px; font-size: 11.5px; letter-spacing: 0.4px; }
  .main-nav a { color: var(--ink); text-decoration: none; }
  .main-nav a.is-current { color: var(--accent); }

  .intro-band { position: absolute; top: 182px; left: 0; width: 1050px; height: 392px; background: var(--band); }
  .intro-painting { position: absolute; left: 141px; top: 59px; width: 365px; height: 274px;
    background: radial-gradient(circle at 48% 52%, #e9e1ea 0%, #7d4d8c 18%, #3d3552 30%, transparent 45%),
                linear-gradient(125deg, #5a2a4a 0%, #c59a3c 30%, #7e6a3a 50%, #c04d7c 75%, #8a2a55 100%); }
  .intro-copy { position: absolute; left: 531px; top: 96px; width: 360px; text-align: center; }
  .intro-title { font-family: "Playfair Display", serif; font-weight: 400; font-size: 29px; color: var(--ink); line-height: 1.2; }
  .intro-copy p { font-size: 9.4px; line-height: 13px; margin-top: 10px; }
  .intro-copy p:first-of-type { margin-top: 32px; }
  .slide-dots { position: absolute; left: 1002px; top: 177px; display: flex; flex-direction: column; gap: 4px; }
  .slide-dots span { width: 7px; height: 7px; border-radius: 50%; border: 1.3px solid var(--ink); }
  .slide-dots span.is-active { background: var(--ink); }

  .explore-title { position: absolute; top: 628px; left: 0; width: 1050px; text-align: center; font-family: "Playfair Display", serif; font-size: 21.5px; font-weight: 400; color: var(--ink); }
  .explore-slogan { position: absolute; top: 662px; left: 0; width: 1050px; text-align: center; font-size: 10.5px; color: var(--muted); }

  .artwork-card { position: absolute; top: 712px; width: 233px; height: 337px; background: var(--card); box-shadow: 0 1px 4px rgba(0,0,0,0.18); padding: 11px; }
  .artwork-card .artwork { width: 100%; height: 100%; }
  .card-one { left: 141px; } .card-two { left: 400px; } .card-three { left: 659px; }
  .art-amber { background: linear-gradient(160deg, #b88a3a 0%, #d7b98a 35%, #c86a2a 55%, #dcd4cc 75%, #b07a3a 100%); }
  .art-blue { background: linear-gradient(180deg, #14244a 0%, #1c3560 25%, #3c6f86 55%, #9a9a8c 80%, #2c6a7c 100%); }
  .art-rose { background: linear-gradient(170deg, #9a3a44 0%, #7c3a34 40%, #b05060 70%, #8a3048 100%); }

  .footer-rule { position: absolute; top: 1114px; left: 0; width: 1050px; height: 1px; background: var(--rule); }
  .social-links { position: absolute; top: 1132px; left: 0; width: 1050px; display: flex; justify-content: center; gap: 12px; list-style: none; }
  .social-links li { display: flex; align-items: center; gap: 4px; font-size: 9px; color: var(--ink); }
  .social-links .dot { width: 23px; height: 23px; border-radius: 50%; background: var(--ink); }
</style>
</head>
<body>
  <header class="brand">
    <div class="brand-name">Mira Castellan Collection</div>
    <div class="brand-tagline">Original Fluid Art Paintings</div>
  </header>

  <nav class="main-nav">
    <a class="is-current" href="#">HOME</a>
    <a href="#">ABOUT</a>
    <a href="#">SHOP</a>
    <a href="#">CART</a>
    <a href="#">CONTACT</a>
  </nav>

  <section class="intro-band">
    <div class="intro-painting" role="img" aria-label="Featured fluid art painting: purple, white and blue bloom on gold and magenta"></div>
    <div class="intro-copy">
      <h1 class="intro-title">A Little bit About Mira</h1>
      <p>I learned I am never too old to re-invent my life. Lesson learned. At the age of 78 and after the ending of my 30 years of marriage I was faced with an unexpected change in my life circumstances. I made the decision to re-invent my life.</p>
      <p>Art, in varying media has always been a part of my experience as a hobby. When I was presented with fluid art, my life as I had known it turned to excitement, and discovery, carving a promising vision of my future.</p>
    </div>
    <div class="slide-dots"><span class="is-active"></span><span></span><span></span><span></span></div>
  </section>

  <h2 class="explore-title">Explore My Creativity</h2>
  <p class="explore-slogan">place for your slogan</p>

  <div class="artwork-card card-one"><div class="artwork art-amber" role="img" aria-label="Fluid art painting in amber, ochre and pale grey cells"></div></div>
  <div class="artwork-card card-two"><div class="artwork art-blue" role="img" aria-label="Fluid art painting with white blooms over deep blue and teal drips"></div></div>
  <div class="artwork-card card-three"><div class="artwork art-rose" role="img" aria-label="Fluid art painting with cream and green blooms on deep rose red"></div></div>

  <div class="footer-rule"></div>
  <ul class="social-links">
    <li><span class="dot"></span>Socialroom</li>
    <li><span class="dot"></span>Chirpline</li>
    <li><span class="dot"></span>Pictaro</li>
    <li><span class="dot"></span>Pinboardly</li>
    <li><span class="dot"></span>Viewtube</li>
  </ul>
</body>
</html>
```